Business card for a Exhibition booth fabrication company

Hi. My company would like to change our corporate name card. We are an events and Exhibition stand builder company. We would like our corporate name card to resonate what we do. I need someone to create something unique that relates to the industry that I am in. The graphic designer should be creative to incorporate the elements of my industry and try to blend in well in the design of the card. Our aim is to ensure that we are unique and our card can look different from our competitors.
Updates

The decision maker was very busy and didnt had time to make this decision

Target Market(s)

Marketing and events manager from all companies

Contact Information for Business Card

The business card should have the following details:
Name
Job Title
Email
Website

Colors

Designer to choose colors to be used in the design.

Requirements
Must have
• The card must be look something that is relevant to the service that I am providing. My website is: www.velmora-buildworks.example
• You can see my website to get more information on what service that I am doing
Nice to have
• On the back of my card, I would like to have a globe image with the incorporation of my company logo. This is to indicate that my services can be done in any part of the world.

```html
<!DOCTYPE html>
<html lang="en">
<head>
<meta charset="utf-8">
<title>Velmora Buildworks – Business Card</title>
<link rel="stylesheet" href="https://fonts.googleapis.com/css2?family=Arimo:wght@400;700&family=Open+Sans:wght@400&display=swap">
<style>
  :root {
    --bg-light: #dadbdd;
    --bg-dark: #a4a5a8;
    --card-black: #000000;
    --brand-red: #ee1c25;
    --band-gray: #6d6e70;
    --line-gray: #8a8a8c;
    --logo-gray: #6a6a6a;
    --white: #ffffff;
    --map-tone: #3c3c3c;
    --map-mid: #2a2a2a;
    --silver: #b4b4b4;
  }
  * { margin: 0; padding: 0; box-sizing: border-box; }
  html, body { width: 1200px; height: 1118px; overflow: hidden; }
  body {
    background: linear-gradient(90deg, var(--bg-light) 0%, var(--bg-dark) 100%);
    position: relative;
    font-family: "Open Sans", Arial, sans-serif;
  }
  .card {
    position: absolute;
    left: 223px;
    width: 754px;
    height: 431px;
    border-radius: 24px;
    overflow: hidden;
    background: var(--card-black);
  }
  .card--front { top: 93px; }
  .card--back { top: 577px; }

  .front-art { position: absolute; inset: 0; width: 754px; height: 431px; display: block; }

  .company-name {
    position: absolute;
    left: 24px;
    top: 158px;
    width: 380px;
    text-align: center;
    font-family: "Arimo", Arial, sans-serif;
    font-weight: 700;
    font-size: 24px;
    letter-spacing: 2.2px;
    color: var(--logo-gray);
  }

  .holder { position: absolute; right: 25px; top: 52px; text-align: right; color: var(--white); font-family: "Arimo", Arial, sans-serif; }
  .holder-name { font-weight: 700; font-size: 24px; letter-spacing: 0.4px; line-height: 1.2; }
  .holder-title { font-weight: 400; font-size: 19px; letter-spacing: 0.6px; margin-top: 3px; }

  .contact-list { position: absolute; right: 25px; top: 308px; list-style: none; color: var(--white); font-size: 18px; }
  .contact-list li { display: flex; align-items: center; justify-content: flex-end; height: 34px; }
  .contact-list svg { width: 19px; height: 19px; margin-left: 12px; fill: var(--white); }

  .address { position: absolute; left: 32px; top: 352px; color: var(--white); font-size: 18px; line-height: 29px; }

  .world-map {
    position: absolute;
    left: 0; top: 60px;
    width: 754px; height: 310px;
    background: radial-gradient(ellipse 60% 55% at 55% 45%, var(--map-tone) 0%, var(--map-mid) 55%, var(--card-black) 100%);
  }
  .back-name {
    position: absolute;
    left: 0; right: 0; top: 212px;
    text-align: center;
    font-family: "Arimo", Arial, sans-serif;
    font-weight: 700;
    font-size: 32px;
    letter-spacing: 3px;
    color: var(--silver);
  }
  .back-web {
    position: absolute;
    left: 0; right: 0; top: 392px;
    text-align: center;
    color: var(--white);
    font-size: 20px;
    letter-spacing: 3.4px;
  }
</style>
</head>
<body>

<section class="card card--front">
  <svg class="front-art" viewBox="0 0 634 362" aria-hidden="true">
    <rect width="634" height="362" fill="var(--card-black)"/>
    <path d="M0,203 C80,248 170,273 260,266 C400,256 520,203 634,208 L634,362 L0,362 Z" fill="var(--white)"/>
    <path d="M0,209 C80,254 170,279 260,272 C400,262 520,209 634,214 L634,362 L0,362 Z" fill="var(--brand-red)"/>
    <path d="M250,265 C400,232 520,182 634,184 L634,205 C520,201 400,244 250,265 Z" fill="var(--band-gray)"/>
    <path d="M392,0 C442,50 430,182 340,236" fill="none" stroke="var(--brand-red)" stroke-width="5"/>
    <path d="M0,0 L382,0 C425,45 418,175 335,225 C270,262 170,262 100,225 C60,205 25,188 0,172 Z" fill="var(--white)" stroke="var(--white)" stroke-width="12"/>
    <path d="M0,0 L382,0 C425,45 418,175 335,225 C270,262 170,262 100,225 C60,205 25,188 0,172 Z" fill="var(--white)" stroke="var(--line-gray)" stroke-width="6"/>
    <path d="M0,0 L382,0 C425,45 418,175 335,225 C270,262 170,262 100,225 C60,205 25,188 0,172 Z" fill="var(--white)" stroke="var(--white)" stroke-width="3"/>
  </svg>

  <div class="company-name">VELMORA BUILDWORKS</div>

  <div class="holder">
    <div class="holder-name">DORIAN KELLER</div>
    <div class="holder-title">PRESIDENT</div>
  </div>

  <div class="address">Street Name, City Name<br>Zipcode - 01234</div>

  <ul class="contact-list">
    <li>012-555-0147
      <svg viewBox="0 0 24 24"><path d="M6.6 10.8a15.1 15.1 0 0 0 6.6 6.6l2.2-2.2c.3-.3.7-.4 1-.2 1.1.4 2.3.6 3.6.6.6 0 1 .4 1 1V20c0 .6-.4 1-1 1A17 17 0 0 1 3 4c0-.6.4-1 1-1h3.5c.6 0 1 .4 1 1 0 1.3.2 2.5.6 3.6.1.3 0 .7-.2 1z"/></svg>
    </li>
    <li>info@velmora-buildworks.example
      <svg viewBox="0 0 24 24"><path d="M2 5h20v14H2z M3 6.5v.4l9 6.2 9-6.2v-.4z" fill-rule="evenodd"/></svg>
    </li>
    <li>www.velmora-buildworks.example
      <svg viewBox="0 0 24 24"><path fill-rule="evenodd" d="M12 2a10 10 0 1 0 0 20 10 10 0 0 0 0-20zm-1 2.1C9.6 5.7 8.8 8 8.7 11H4.1A8 8 0 0 1 11 4.1zm2 0A8 8 0 0 1 19.9 11h-4.6c-.1-3-.9-5.3-2.3-6.9zM10.7 11c.1-2.7.6-4.6 1.3-5.8.7 1.2 1.2 3.1 1.3 5.8zM4.1 13h4.6c.1 3 .9 5.3 2.3 6.9A8 8 0 0 1 4.1 13zm6.6 0h2.6c-.1 2.7-.6 4.6-1.3 5.8-.7-1.2-1.2-3.1-1.3-5.8zm4.6 0h4.6a8 8 0 0 1-6.9 6.9c1.4-1.6 2.2-3.9 2.3-6.9z"/></svg>
    </li>
  </ul>
</section>

<section class="card card--back">
  <div class="world-map" role="img" aria-label="Dark grey world map across the card, showing that stands are built anywhere in the world"></div>
  <div class="back-name">VELMORA BUILDWORKS</div>
  <div class="back-web">www.velmora-buildworks.example</div>
</section>

</body>
</html>
```